Need home page concept design for existing website

Our existing website is www.quillbyte.com. We started re-branding project. We need one page (home page) concept made in Photoshop with a new theme. PLEASE REVIEW THE MOCK-UP OF NEW HOME PAGE IN THE ATTACHED MS DOC FILE.

We develop data processing productivity software for corporate clients. By purchasing our products and services our customers gain efficiency, cut cost, free up resources.

The new theme and styles should be modern responsive (compatible with mobile devices). Our current website's home page has lots of descriptive information which create a sense of clutter.

The new design should be clear and distinct. I like ArtHarbor.com color theme, font styles and menus. Another one I like http://velmicor.com/ - the style, theme and the way they convey complicated idea to prospects.

Industry/Entity Type

Software

Font styles to use
Sans Serif

Requirements
Must have
• Clearness. Modern style. Responsive. Innovative business style that will convey new fresh approach to traditional problems our customers have. However it should not be too much extravagant, to scare off our corporate customers.

```html
<!DOCTYPE html>
<html lang="en">
<head>
<meta charset="utf-8">
<title>Quillbyte – Productivity Solutions for Norvex ERP</title>
<link href="https://fonts.googleapis.com/css2?family=PT+Sans:wght@400;700&family=Questrial&family=Signika:wght@600&display=swap" rel="stylesheet">
<style>
:root{
  --blue:#2a7ab8;
  --blue-dark:#1d6aa6;
  --green:#17922f;
  --green-dark:#0f7a24;
  --ink:#222;
  --text:#333;
  --dark-bg:#1c1c1c;
  --light-bg:#efefef;
  --panel:#ffffff;
  --foot-link:#9a9a9a;
  --red:#c4161c;
}
*{box-sizing:border-box;margin:0;padding:0}
html,body{width:1005px;height:1200px;overflow:hidden}
body{position:relative;background:var(--dark-bg);font-family:"PT Sans",sans-serif;color:var(--text)}
a{color:inherit;text-decoration:none}

.top-area{position:absolute;left:0;top:0;width:1005px;height:559px;background:linear-gradient(#f3f3f3,#ececec)}
.site-header{position:absolute;left:0;top:0;width:1005px;height:109px}
.brand{position:absolute;left:85px;top:14px}
.brand-name{font-family:"Signika",sans-serif;font-weight:600;font-size:44px;line-height:46px;color:var(--ink);letter-spacing:-0.5px}
.brand-tag{font-size:12px;color:var(--ink);margin-top:2px}
.cta{position:absolute;top:39px;height:35px;border-radius:4px;font-family:"Questrial",sans-serif;font-size:19px;color:#fff;display:flex;align-items:center;justify-content:center;font-weight:700}
.cta-trial{left:573px;width:162px;background:linear-gradient(#3a3a3a,#222);border:2px solid #555}
.cta-quote{left:755px;width:162px;background:linear-gradient(#1ea53a,var(--green-dark));border:2px solid #2fb84a}

.main-nav{position:absolute;left:0;top:109px;width:1005px;height:46px;background:var(--blue)}
.main-nav ul{list-style:none;display:flex;position:absolute;left:86px;top:0;height:46px}
.main-nav li{height:46px;display:flex;align-items:center;padding:0 12px;font-size:12px;color:#fff;border-right:1px solid #4a8fc6;letter-spacing:-0.2px;white-space:nowrap}
.main-nav li:first-child{padding-left:17px}
.main-nav li:last-child{border-right:none}
.search{position:absolute;left:724px;top:11px;width:178px;height:24px;background:#fff;border-radius:3px;font-size:9.5px;color:#999;padding:6px 8px}
.search svg{position:absolute;right:7px;top:5px}

.intro{position:absolute;left:86px;top:176px;width:840px}
.intro h1{font-size:20px;font-weight:400;color:var(--ink);letter-spacing:0.2px}
.intro p{margin-top:12px;font-size:12.6px;line-height:20px;color:var(--text);padding-left:2px;letter-spacing:0.2px}

.panel{position:absolute;left:85px;top:332px;width:835px;height:800px;background:var(--panel);border-radius:7px}
.feature{position:absolute;left:11px;top:14px;width:560px}
.feature-title{font-family:"PT Sans",sans-serif;font-weight:700;font-size:80px;line-height:70px;color:var(--blue-dark);letter-spacing:-3.5px;padding-left:26px;white-space:nowrap}
.feature-sub{font-size:20px;color:var(--ink);text-align:right;padding-right:16px;margin-top:2px;letter-spacing:-0.3px}
.feature-photo{position:absolute;left:11px;top:124px;width:561px;height:319px;background:linear-gradient(160deg,#f6f6f6 20%,#d9cbbd 55%,#8b7b6c 85%,#4a4440)}
.video-link{position:absolute;left:11px;top:451px;font-size:11px;color:var(--red);text-decoration:underline}
.feature-text{position:absolute;left:11px;top:468px;width:560px;font-size:11.5px;line-height:17px;color:var(--ink)}
.col-head{font-size:12.5px;font-weight:700;color:var(--green);letter-spacing:0.3px}
.overview{position:absolute;left:11px;top:524px;width:210px}
.overview p{margin-top:10px;padding-left:2px;font-size:11.5px;line-height:17px;color:var(--ink)}
.modules{position:absolute;left:242px;top:524px}
.modules ul{margin-top:8px;list-style:none}
.modules li{font-size:11.5px;line-height:18.5px;color:var(--ink);padding-left:8px;position:relative}
.modules li::before{content:"";position:absolute;left:0;top:8px;width:2px;height:2px;background:var(--ink)}

.sidebar{position:absolute;left:587px;top:0;width:248px;height:640px;background:linear-gradient(90deg,#eaeaea,#f8f8f8 8%,#fafafa);border-radius:0 7px 0 0}
.event-title{position:absolute;left:0;top:14px;width:238px;text-align:center;font-family:"Signika",sans-serif;font-weight:600;font-size:35px;line-height:39px;color:var(--blue);letter-spacing:1.5px}
.event-info{position:absolute;left:25px;top:111px;font-family:Arial,sans-serif;font-size:12px;line-height:18.5px;color:var(--ink)}
.event-info .strong{font-weight:700}
.event-info .reg{padding-left:35px;font-weight:700}
.side-btn{position:absolute;left:23px;width:203px;height:55px;border-radius:4px;font-family:"Questrial",sans-serif;color:#fff;font-size:19.5px;line-height:23px;text-align:center;display:flex;align-items:center;justify-content:center;letter-spacing:1px}
.btn-signup{top:226px;background:linear-gradient(#3a8ed0,#1a6aa8);border:1px solid #5aa5dc}
.btn-past{top:316px;background:linear-gradient(#1ea53a,var(--green-dark));border:1px solid #3dc255}
.btn-request{top:412px;background:#1d1d1d;border:1px solid #444}

.solutions{position:absolute;left:12px;top:650px;width:810px;height:134px;background:#f4f4f4;border-radius:5px}
.solution{position:absolute;top:10px}
.solution h2{font-size:16.5px;font-weight:700;color:var(--blue);letter-spacing:0.5px}
.solution .thumb{position:absolute;top:24px;width:124px;height:83px}
.solution p{position:absolute;top:26px;font-size:11.5px;line-height:17px;color:var(--ink)}
.web{left:14px}
.web .thumb{left:0;background:linear-gradient(135deg,#e9eef2,#b8c3cc 50%,#3b3f47)}
.web p{left:133px;width:200px}
.output{left:411px;top:12px}
.output .thumb{left:0;top:23px;background:linear-gradient(160deg,#d6e4ee,#9bb5c8 50%,#5d7489)}
.output p{left:135px;width:245px;top:24px}
.divider{position:absolute;left:395px;top:16px;height:104px;border-left:1px dotted #b5b5b5}

.site-footer{position:absolute;left:0;top:1143px;width:1005px;text-align:center;font-family:Arial,sans-serif}
.footer-links{font-size:12px;color:var(--foot-link);word-spacing:1px}
.footer-links span{padding:0 8px}
.copyright{margin-top:10px;font-size:10.5px;color:var(--foot-link)}
</style>
</head>
<body>
<div class="top-area">
  <header class="site-header">
    <div class="brand">
      <div class="brand-name">Quillbyte</div>
      <div class="brand-tag">Easy Productivity Solutions for Managing Your Norvex ERP Data</div>
    </div>
    <a class="cta cta-trial" href="#">Get a FREE Trial</a>
    <a class="cta cta-quote" href="#">Request A Quote</a>
  </header>
  <nav class="main-nav">
    <ul>
      <li>HOME</li>
      <li>DATA LOADERS FOR NORVEX</li>
      <li>WEB SOLUTIONS FOR NORVEX</li>
      <li>ABOUT US</li>
      <li>CONTACT US</li>
    </ul>
    <div class="search">Search here...
      <svg width="13" height="13" viewBox="0 0 13 13"><circle cx="5.5" cy="5.5" r="4" fill="none" stroke="#aaa" stroke-width="2"/><line x1="8.5" y1="8.5" x2="12" y2="12" stroke="#aaa" stroke-width="2.2" stroke-linecap="round"/></svg>
    </div>
  </nav>
  <section class="intro">
    <h1>Quickly and Safely Manage Complex Norvex Tasks and Significantly Increase Efficiency</h1>
    <p>Your company needs to be nimble. Your customers demand it. Your competition challenges it. Your survival depends on it. Don’t get bogged down by cumbersome Norvex ERP tasks when Quillbyte’s easy-to-use, safe and simple solutions can triple your productivity.</p>
  </section>
</div>

<main class="panel">
  <section class="feature">
    <div class="feature-title">DATA LOADER</div>
    <div class="feature-sub">Productivity Solutions for Norvex ERP</div>
  </section>
  <div class="feature-photo" role="img" aria-label="Business team meeting around a round conference table"></div>
  <a class="video-link" href="#">(Or Sales Video)</a>
  <p class="feature-text">Download your Norvex ERP data into easy-to-use Gridsheet spreadsheets where you can make massive changes and upload them safely to back Norvex.</p>

  <div class="overview">
    <div class="col-head">OVERVIEW</div>
    <p>Find out more about what makes Data Loaders the perfect solution for Norvex data management!</p>
  </div>
  <div class="modules">
    <div class="col-head">BROWSE OUR DATA LOADER MODULES</div>
    <ul>
      <li>Finance</li>
      <li>Distribution &amp; Supply Chain</li>
      <li>Master Data &amp; Inventory</li>
      <li>Production</li>
    </ul>
  </div>

  <aside class="sidebar">
    <div class="event-title">UPCOMING<br>EVENT</div>
    <div class="event-info">
      <div class="strong">Webinars</div>
      <div>Transforming Your Fiscal EOY<br>Process</div>
      <div>Jan 15, 2014 at 1:00 PM EST</div>
      <div class="reg">(click Box): Register</div>
    </div>
    <a class="side-btn btn-signup" href="#">Sign Up For<br>FREE WEBINARS</a>
    <a class="side-btn btn-past" href="#">PAST WEBINARS</a>
    <a class="side-btn btn-request" href="#">Request A<br>WEBINARS</a>
  </aside>

  <section class="solutions">
    <div class="solution web">
      <h2>WEB SOLUTIONS</h2>
      <div class="thumb" role="img" aria-label="Two colleagues reviewing documents with a laptop"></div>
      <p>Access Norvex ERP data from anywhere on any mobile device to check inventory, purchase orders and more. For both Norvex users and non-users</p>
    </div>
    <div class="divider"></div>
    <div class="solution output">
      <h2>OUTPUT SOLUTIONS</h2>
      <div class="thumb" role="img" aria-label="Office team working together at a bright desk"></div>
      <p>From outputting easy information-sharing documents to dynamic print solutions, Quillbyte output solutions for Norvex ERP greatly improve your efficiency.</p>
    </div>
  </section>
</main>

<footer class="site-footer">
  <div class="footer-links">Home<span>|</span>Blog<span>|</span>Gridsheet Loaders for Norvex<span>|</span>QuillPrint<span>|</span>FormBox PDF and Gridsheet Service<span>|</span>Web Solutions for Norvex<span>|</span>Contact Us</div>
  <div class="copyright">© 2015 - Quillbyte | Site by tern web studio | Privacy Policy | Site Information</div>
</footer>
</body>
</html>
```